Attorney--Animal Law & Equine Law Litigation & Mediation

Card should read:

Marisol T. R. Quenby, Ph.D., Esq.
Attorney at Law

Back side should reference: Quenby Law Group:
Animal Law, Equine Law, Litigation and Mediation Services

Some small animal-related logo on the back with the above information, showing mixed animals, with a horse in there. Please see samples.

Please see sample cards for front-side view. Something clean and simple. Solid color with text in white. Small logo on front possibly OK.

Can abbreviate Quenby Law Group to QLG

Text also should have address; phone number; website name: www.QuenbyLawGroup.example

Target Market(s)

Attorneys; equine market

Industry/Entity Type

Attorney

Contact Information for Business Card

Marisol T. R. Quenby

Font styles to use
Sans Serif

Colors
0356a4
6b449b

Requirements
Nice to have
• I really like the image I included that has multiple animals, and LAW in big letters. I would change the LAW to QLG (for Quenby Law Group) and then spell out Quenby Law Group under the image perhaps??

```html
<!DOCTYPE html>
<html lang="en">
<head>
<meta charset="utf-8">
<title>Quenby Law Group Business Card</title>
<link rel="stylesheet" href="https://fonts.googleapis.com/css2?family=PT+Sans:wght@400;700&display=swap">
<style>
  :root {
    --backdrop: #e9e7e3;
    --brand-blue: #0356a4;
    --brand-purple: #6b449b;
    --paper: #ffffff;
    --paper-shade: #f1f0f5;
    --on-brand: #ffffff;
    --on-brand-soft: rgba(255,255,255,.82);
    --rule-light: rgba(255,255,255,.7);
  }
  * { margin: 0; padding: 0; box-sizing: border-box; }
  html, body { width: 1200px; height: 780px; overflow: hidden; }
  body {
    background: var(--backdrop);
    font-family: "PT Sans", sans-serif;
    position: relative;
  }
  .card {
    position: absolute;
    top: 235px;
    width: 540px;
    height: 310px;
    border-radius: 18px;
    box-shadow: 0 2px 0 #d8d8d8, 0 4px 0 #cfcfcf, 0 8px 18px rgba(0,0,0,.18);
    overflow: hidden;
  }
  .card--front {
    left: 45px;
    background: var(--brand-blue);
    color: var(--on-brand);
  }
  .card--back {
    left: 615px;
    background: linear-gradient(135deg, var(--paper) 0%, var(--paper-shade) 100%);
  }

  /* Firm mark: name with one plain circle */
  .mark { display: flex; align-items: center; gap: 12px; }
  .mark__dot { border-radius: 50%; flex: none; }
  .mark__name { font-weight: 700; line-height: 1; white-space: nowrap; }

  .card--front .mark { position: absolute; left: 32px; top: 36px; }
  .card--front .mark__dot { width: 40px; height: 40px; background: var(--on-brand); }
  .card--front .mark__name { font-size: 22px; color: var(--on-brand); }

  .holder {
    position: absolute;
    right: 36px;
    top: 110px;
    font-size: 21px;
    font-weight: 700;
    text-align: right;
    white-space: nowrap;
  }
  .divider {
    position: absolute;
    left: 130px;
    right: 36px;
    top: 145px;
    height: 1px;
    background: var(--rule-light);
  }
  .role {
    position: absolute;
    right: 36px;
    top: 152px;
    font-size: 15px;
    color: var(--on-brand-soft);
  }
  .contacts {
    position: absolute;
    left: 32px;
    bottom: 28px;
    list-style: none;
    font-size: 14px;
  }
  .contacts li { display: flex; align-items: center; gap: 8px; line-height: 22px; }
  .contacts svg { width: 15px; height: 15px; flex: none; }
  .address {
    position: absolute;
    right: 36px;
    bottom: 39px;
    text-align: right;
    font-size: 14px;
    line-height: 22px;
    font-style: normal;
  }

  .card--back .stack {
    position: absolute;
    inset: 0;
    display: flex;
    flex-direction: column;
    align-items: center;
    justify-content: center;
    gap: 16px;
  }
  .card--back .mark__dot { width: 52px; height: 52px; background: var(--brand-purple); }
  .card--back .mark__name { font-size: 30px; color: var(--brand-blue); }
  .back-rule { width: 260px; height: 2px; background: var(--brand-purple); }
  .services {
    text-align: center;
    color: var(--brand-purple);
    font-size: 16px;
    line-height: 24px;
  }
</style>
</head>
<body>
  <section class="card card--front" aria-label="Business card front">
    <div class="mark">
      <span class="mark__dot"></span>
      <span class="mark__name">Quenby Law Group</span>
    </div>

    <p class="holder">Marisol T. R. Quenby, Ph.D., Esq.</p>
    <div class="divider"></div>
    <p class="role">Attorney at Law</p>

    <ul class="contacts">
      <li>
        <svg viewBox="0 0 16 16" aria-hidden="true"><rect width="16" height="16" rx="3" fill="#fff"/><path d="M5 4h2l1 2.5-1.2 1a6 6 0 0 0 2.7 2.7l1-1.2L13 10v2a1 1 0 0 1-1 1A8 8 0 0 1 4 5a1 1 0 0 1 1-1z" fill="#0356a4"/></svg>
        555-014-2290
      </li>
      <li>
        <svg viewBox="0 0 16 16" aria-hidden="true"><rect width="16" height="16" rx="3" fill="#fff"/><rect x="3" y="4.5" width="10" height="7" fill="none" stroke="#0356a4" stroke-width="1.2"/><path d="M3 4.5l5 4 5-4" fill="none" stroke="#0356a4" stroke-width="1.2"/></svg>
        info@quenbymail.example
      </li>
      <li>
        <svg viewBox="0 0 16 16" aria-hidden="true"><rect width="16" height="16" rx="3" fill="#fff"/><circle cx="8" cy="8" r="4.8" fill="none" stroke="#0356a4" stroke-width="1.1"/><ellipse cx="8" cy="8" rx="2" ry="4.8" fill="none" stroke="#0356a4" stroke-width="1"/><path d="M3.2 8h9.6" stroke="#0356a4" stroke-width="1"/></svg>
        www.QuenbyLawGroup.example
      </li>
    </ul>

    <address class="address">
      PO BOX 4410 W. 12th St.,<br>
      #210 Larkfield, TX 00000 USA
    </address>
  </section>

  <section class="card card--back" aria-label="Business card back">
    <div class="stack">
      <div class="mark">
        <span class="mark__dot"></span>
        <span class="mark__name">Quenby Law Group</span>
      </div>
      <div class="back-rule"></div>
      <p class="services">
        Animal Law &middot; Equine Law<br>
        Litigation and Mediation Services
      </p>
    </div>
  </section>
</body>
</html>
```